International trading company needs banner designs for university careers fairs. Additional work to

Description
Our company, Meridale Capital, operates in the finance industry. We trade numerous financial instruments across the globe. We focus on futures, options, etfs and are currently expanding into the exciting area of cryptocurrencies. A main focus of ours is to use a systematic and quantitative approach to trading to develop and refine trading strategies that are relatively low risk in nature, but are scalable and provide positive returns. We work hard, we push each other to achieve great results. But at the same time we really enjoy each other’s company and share a relaxed atmosphere at work. Our website is http://www.meridalecapital.com.au/. Meridale will be attending university careers fairs and expos in coming months to attract the very best talent there is for graduate trading roles as well as graduate developer roles. As such, we require our booth to look professional. We want to convey our message that a career with us is exciting, rewarding, but also challenging. We aim to nurture talent and hope to provide the tools necessary to strive in a career in trading.

We have 3 aspects to our booth concept. But for this designer contest, we will focus on 1 of those projects. When we decide on one designer, we hope they will be willing to work one on one on the other 2 projects. On top of this contest, we are willing to pay $250 for the additional 2 projects, one of which is quite simple in design brief, the other will allow the designer the flare to be creative. It is important to note that all three concepts need to be cohesive. Each concept should complement the other in colour as well as message.

For the entire project to be finished, we are a little rushed on time and would require completion of all three concepts by February 2nd.

We will only require soft copy files so we can manage the print ourselves. We can accept a vector, eps or ai file.

For this contest project, the design concept is a pull-up banner. We will have 3 pull-up banners each with slightly different messages.

We have attached pictures to help inspire the designer. Also, we have attached company logo (a unicorn) and name, along with varying colour vectors.

Meridale Capital’s primary colours are black, green and white. We would like all 3 banners to be in the same scheme. But we are happy to see slightly different variations in design options on the colour scheme. We do feel that green writing on black background would look the sharpest and have the most impact. We could be wrong though and are fine to see different designs.

The banner dimensions will be 85cm wide x 210cm tall. So there is room on the banner to deliver an exciting, yet professional message.

Preliminary Pull-up Banner ideas
We are not designers, we are open to you, the designer, using your creative flare to design 3 sharp looking banners. We do have a rough idea of the direction of each banner though.

Banner 1 – A company inspired banner. We would like our company name, our logo (prominent!) and beneath it 3 to 4 words that describe what we’re about. For example, Challenging, Rewarding, Passionate, Entrepreneurial, Focused, Collaborative, Innovative, Systematic, Strategic. Happy for the designer to take control here.

For the rest of the banner we are open to design. Potentially a picture taken from our website that is reflective of our culture – which is relaxed, hard-working, collaborative, rewarding.

It doesn’t need to be too busy or cluttered, so no need to throw in designs that aren’t really consistent with us.

Banner 2 – A trader inspired banner. This is more designed to attract graduates interested in a career in trading. Include meridale name and logo. Maybe include a question for the students... Something like,
“Want to be challenged?
Want to strategise?
Want to be rewarded?
Become a trader!”
Doesn’t have to be straight angles, can be on an angle – designer free reign here. Also we can have different sentences, words. Up to the designer. We would like to include something that would attract a trader’s mind, something visual, like a trading chart. See attached pictures for trading chart examples.

Somewhere on the banner we can mention Graduate Markets Pathway, please contact us at careers@meridalecapital.com.au. Phone number below it (02) 7416 5830.

Banner 3 - A developer inspired banner. This is more designed to attract graduates interested in a career in developing. Include meridale name and logo

Put the following pitch on the banner and fill the rest of the space with designs and pictures. No fixed layout required here.

Good at problem solving? Obsessed with creating quality software? Love working with numbers? Do you speak programming language? Want to face fresh challenges each day?

On the banner we can mention Graduate Systems Builder Pathway, please contact us at careers@meridalecapital.com.au. Phone number below it (02) 7416 5830.

Additionally to the above 3 banners, we had an idea of including random words across the banners in random sizes and boldness. We’re not sure how this would appear so we would like to see a couple designs on this. We thought we could have a top tier of buzz words that should be more prominent with the second tier buzzwords in smaller size. Two design types - randomly displayed, secondly a bit more structured. Can decide what looks best when we receive design. Words below. We don’t have to include all of these words, whatever a good design lends itself to. Words should only be in green, black or white - consistent with our company scheme.

Top Tier Buzzwords
Trading
Cryptocurrency
Options
Market making
Trading
Plinkmark
Derivatives
ETF
Futures
Volatility
Arbitrage
Technology
HFT
Hedging

Second Tier Buzzwords
T&R 400
BQZ 150
VWL
MYT
BQZ
FX
Bid
Offer
Margining
Long
Short
Spot
Position
Torvane
Dulmar
Pel Varo
PVI
QRN
Buy
Sell
Delta
Gamma
Vega
Theta
Skew
Straddle
Call

Once we have selected the designer, we are keen that they would complete another 2 projects for us. The other 2 projects are as follows:
• A double sided A5 flyer design – This should provide more information about what Meridale can offer the students as a career and a workplace. We will also give a small amount of detail about the graduate program.
• Table Cloth design – At each exhibition we receive a table at our booth. We would like to have a logo laden table cloth that will look professional

We would like the design scheme to flow neatly from the banners to the flyers to the table cloth. So the colours are consistent and our general tone/message is also consistent.

We have attached pictures that should help the designer. Included pictures of pull-up banners, pictures of student careers fairs, flyers, table cloth dimensions, Meridale’s logos and colour vectors.

Preliminary Double sided A5 Flyer ideas.

We would need two designs – a trader design and a developer design.

Art file to be supplied PDF file with trim marks & 3mm bleed

With the flyer we would like to add a little more information about Meridale on the front page (which should be the same for the trader flyer and the developer flyer). On the back page we would be a little more detailed in the graduate program. Give dates, the onboarding process, rough program details/info.

Front Page – Include Meridale name, logo. Explanation of who we are - proprietary trading firm, using our own capital to trade financial instruments around the world. We trade futures, options, etfs and cryptocurrencies (can make more elaborate).

To make it sound interesting we’d like to explain potential for growth in certain markets. So something along the lines, of “We are seeing rapid expansion in certain markets. At meridale we are always looking for new strategies and talent to expand our already growing presence. Working with Meridale, you’ll get exposure and experience on all of these exciting markets which will greatly benefit you in your career progression” (Doesn’t need to be word for word)

We’d also like to mention some of the perks of working with us:
daily lunch provided
cafe coffee
 breakfast/snacks
 casual attire
 cash bonus half yearly
 competitive rates
 team dinners
 gym membership
 company trips
We’d like to use consistent colour schemes with our company, Black and Green. Some white could work in there. But not a necessity.
The designer can feel free to add in some sharp looking images.

Back Page Trader Flyer - We would like to give some more info on the positives of the trader program. We’re mainly focusing on the strengths of the program here – listed below.
• 1 on 1 training
• In-depth theory classes with practical applications
• Experienced traders providing the training
• Live trading within 3 months
• Ongoing mentoring
• Exposure to different markets/strategies
• Placed onto products that best suit their strengths
• Simulated trader training based on actual events

We should also add contact details for students to apply to.
For more information on the Graduate Markets Pathway
contact us at careers@meridalecapital.com.au.
Phone number (02) 7416 5830.

OR

To apply please send through your CV and academic transcript to careers@meridalecapital.com.au

We would also want this to look quite sharp, so adding in a trading graph could make it look exciting and attractive.

Back Page Developer Flyer
• 1 on 1 mentoring by senior software engineers
• Full SDLC exposure
• Extremely agile environment
• Direct interaction with business and stakeholders
• Multiple career paths for future growth

For more information on the Graduate Systems Builder Pathway
Contact us at careers@meridalecapital.com.au.

OR

Preliminary table cloth ideas.
We would need two designs before choosing one.

First design is a very simple design that would look professional. A plain black design with MERIDALE on the front in Green.

The second design is plain black, MERIDALE on the front in Green, similar to above. But we’d also like to see the words mentioned above in the top tier and second tier randomly across the table cloth. In different sizes and weightings.
We’ll see which design looks the best and choose one.

References to see the products we’d be using:
https://bannoroft.com.au/products/pull-up-banners
https://www.folderquill.com.au/flyers/design
https://www.tabletorvo.com.au/outdoor/custom-table-throws/loose-printed-table-throws.html

Target Market(s)

University Graduates in IT, Engineering, Maths, Sciences, Business that would be interested in a career of trading financial instruments including cryptocurrency, options, futures, ETFs. We are also targeting developers in the same space.

Industry/Entity Type

Finance

Font styles to use
Serif
Sans Serif

Colors
00a990
ffffff
000000
33b8a4
1b1b1b

Requirements
Must have
• Cohesion between banners and other project work.
• Clear message coming through
• Professional look
• Eye catching
• Attractive
• Colour schemes must work
Should not have
• Must not be boring. We are looking to project our company image. We are not boring so we want to see some creative flare. But we are also a professional firm so our designs must be sharp.

```html
<!DOCTYPE html>
<html lang="en">
<head>
<meta charset="utf-8">
<title>Meridale Capital – Pull-up Banner</title>
<link href="https://fonts.googleapis.com/css2?family=Josefin+Sans:wght@300&family=Oswald:wght@400&family=Roboto:wght@400;700&display=swap" rel="stylesheet">
<style>
  :root{
    --stage:#e6e7e8;
    --black:#000000;
    --ink:#1b1b1b;
    --white:#ffffff;
    --green:#33b8a4;
    --green-deep:#00a990;
    --green-bright:#3fd0a6;
  }
  html,body{margin:0;padding:0;width:1200px;height:1000px;overflow:hidden;background:var(--stage);}
  .banner{position:absolute;left:419px;top:55px;width:362px;height:890px;overflow:hidden;background:var(--black);box-shadow:0 6px 24px rgba(0,0,0,.25);}
  .banner-shapes{position:absolute;inset:0;width:362px;height:890px;}
  .brand-name{position:absolute;left:0;right:0;top:48px;text-align:center;margin:0;
    font-family:"Josefin Sans",sans-serif;font-weight:300;font-size:44px;letter-spacing:1px;color:var(--green-deep);}
  .values{position:absolute;left:74px;top:200px;margin:0;padding:0;list-style:none;}
  .value{display:flex;align-items:center;height:62px;margin-bottom:9px;}
  .value-icon{width:62px;height:62px;flex:none;}
  .value-label{margin-left:17px;font-family:"Oswald",sans-serif;font-size:24px;color:var(--green-bright);letter-spacing:.3px;}
  .web{position:absolute;left:0;right:0;top:812px;text-align:center;
    font-family:"Roboto",sans-serif;font-size:17px;color:var(--ink);}
  .web b{font-weight:700;}
</style>
</head>
<body>
<main class="banner">
  <svg class="banner-shapes" viewBox="0 0 362 890" aria-hidden="false">
    <defs>
      <linearGradient id="photoTone" x1="0" y1="0" x2="1" y2="0">
        <stop offset="0" stop-color="#7d7a74"/>
        <stop offset=".45" stop-color="#3a3f5a"/>
        <stop offset="1" stop-color="#bdbbb4"/>
      </linearGradient>
      <linearGradient id="photoFade" x1="0" y1="0" x2="0" y2="1">
        <stop offset="0" stop-color="#000" stop-opacity="1"/>
        <stop offset=".45" stop-color="#000" stop-opacity=".35"/>
        <stop offset="1" stop-color="#000" stop-opacity="0"/>
      </linearGradient>
    </defs>
    <rect class="field" width="362" height="890" fill="var(--black)"/>
    <rect class="team-photo" x="0" y="380" width="362" height="380" fill="url(#photoTone)" role="img" aria-label="Photo of two team members working together at trading desks"/>
    <rect x="0" y="380" width="362" height="200" fill="url(#photoFade)"/>
    <path class="top-band" d="M0 122 C150 195 270 180 362 132 V150 C270 198 150 210 0 140Z" fill="var(--green)"/>
    <path class="top-panel" d="M0 0 H362 V128 C270 172 150 188 0 122Z" fill="var(--white)"/>
    <path class="wave-thin" d="M0 690 C120 668 250 668 362 618 V636 C250 690 120 700 0 712Z" fill="var(--green)"/>
    <path class="wave-dark" d="M0 708 C120 696 250 688 362 632 V890 H0Z" fill="var(--black)"/>
    <path class="footer-panel" d="M0 768 C140 748 260 755 362 712 V890 H0Z" fill="var(--green)"/>
  </svg>

  <h1 class="brand-name">MERIDALE</h1>

  <ul class="values">
    <li class="value">
      <svg class="value-icon" viewBox="0 0 62 62"><circle cx="31" cy="31" r="29" fill="none" stroke="var(--green-bright)" stroke-width="2"/><circle cx="31" cy="31" r="23" fill="none" stroke="var(--green-bright)" stroke-width="1"/>
        <path d="M19 32 C17 24 24 19 31 20 C39 18 46 24 43 32 C44 38 38 41 33 40 L33 44 L29 44 L29 40 C23 41 18 38 19 32Z" fill="var(--green-bright)"/></svg>
      <span class="value-label">CHALLENGING</span>
    </li>
    <li class="value">
      <svg class="value-icon" viewBox="0 0 62 62"><circle cx="31" cy="31" r="29" fill="none" stroke="var(--green-bright)" stroke-width="2"/><circle cx="31" cy="31" r="23" fill="none" stroke="var(--green-bright)" stroke-width="1"/>
        <rect x="19" y="25" width="24" height="6" fill="var(--green-bright)"/><rect x="21" y="32" width="20" height="12" fill="var(--green-bright)"/>
        <rect x="29.5" y="25" width="3" height="19" fill="var(--black)"/>
        <path d="M31 25 C27 18 21 20 24 24 Z M31 25 C35 18 41 20 38 24 Z" fill="none" stroke="var(--green-bright)" stroke-width="2"/></svg>
      <span class="value-label">REWARDING</span>
    </li>
    <li class="value">
      <svg class="value-icon" viewBox="0 0 62 62"><circle cx="31" cy="31" r="29" fill="none" stroke="var(--green-bright)" stroke-width="2"/><circle cx="31" cy="31" r="23" fill="none" stroke="var(--green-bright)" stroke-width="1"/>
        <circle cx="30" cy="32" r="12" fill="none" stroke="var(--green-bright)" stroke-width="2.5"/><circle cx="30" cy="32" r="6.5" fill="none" stroke="var(--green-bright)" stroke-width="2.5"/><circle cx="30" cy="32" r="2" fill="var(--green-bright)"/>
        <path d="M30 32 L42 20 M38 19 L43 19 L43 24" fill="none" stroke="var(--green-bright)" stroke-width="2"/></svg>
      <span class="value-label">FOCUSED</span>
    </li>
    <li class="value">
      <svg class="value-icon" viewBox="0 0 62 62"><circle cx="31" cy="31" r="29" fill="none" stroke="var(--green-bright)" stroke-width="2"/><circle cx="31" cy="31" r="23" fill="none" stroke="var(--green-bright)" stroke-width="1"/>
        <path d="M31 22 C25 22 22 26 22 30 C22 34 26 36 27 39 H35 C36 36 40 34 40 30 C40 26 37 22 31 22Z" fill="none" stroke="var(--green-bright)" stroke-width="2"/>
        <path d="M27 42 H35 M28 45 H34 M31 15 V18 M20 20 L22 22 M42 20 L40 22 M16 30 H19 M43 30 H46" stroke="var(--green-bright)" stroke-width="2"/></svg>
      <span class="value-label">INNOVATIVE</span>
    </li>
  </ul>

  <p class="web" style="margin:0">www.<b>meridalecapital</b>.com.au</p>
</main>
</body>
</html>
```